KLV Business Card - Courier/Transportation - Needs Double Sided Business Card

I am searching for business cards for my company. Currently I just need cards for the (3) founders.

We are a new courier/transporation company that specializes in the medical/pharmaceutical arena.

As you will see from our logo, our primary colors are green and black. We strive to have an efficient, streamlined service offering. I like traditional looks, but also want to showcase our young, modern feel. I would like our card to be double sided.

Target Market(s)

Pharmacies
Hospitals
Physcian Office
Labs

Industry/Entity Type

Business

```html
<!DOCTYPE html>
<html lang="en">
<head>
<meta charset="utf-8">
<title>KLV Courier – Business Card</title>
<link href="https://fonts.googleapis.com/css2?family=Roboto+Condensed:wght@400;700&display=swap" rel="stylesheet">
<style>
  :root {
    --brand-green: #10b02a;
    --ink: #555555;
    --logo-dark: #2f2f2f;
    --paper: #ffffff;
    --backdrop-light: #f8f8f8;
    --backdrop-dark: #e2e2e2;
  }
  * { margin: 0; padding: 0; box-sizing: border-box; }
  html, body { width: 1200px; height: 948px; overflow: hidden; }
  body {
    position: relative;
    background: radial-gradient(ellipse at center, var(--backdrop-light) 0%, var(--backdrop-light) 45%, var(--backdrop-dark) 100%);
    font-family: "Roboto Condensed", "Arial Narrow", sans-serif;
  }
  .card {
    position: absolute;
    left: 262px;
    width: 675px;
    height: 337px;
  }
  .card-front {
    top: 118px;
    background: var(--brand-green);
    display: flex;
    align-items: center;
    justify-content: center;
  }
  .card-back {
    top: 493px;
    background: var(--paper);
    border: 1px solid var(--brand-green);
  }
  .wordmark {
    font-weight: 700;
    letter-spacing: 2px;
    line-height: 1;
    white-space: nowrap;
  }
  .card-front .wordmark {
    color: var(--paper);
    font-size: 46px;
    margin-top: -18px;
  }
  .card-back .wordmark {
    position: absolute;
    left: 88px;
    top: 126px;
    color: var(--logo-dark);
    font-size: 44px;
  }
  .identity {
    position: absolute;
    left: 403px;
    top: 38px;
    color: var(--ink);
  }
  .identity .company { font-size: 21px; line-height: 26px; }
  .identity .role { font-size: 16px; line-height: 20px; }
  .contact-list {
    position: absolute;
    left: 366px;
    top: 168px;
    list-style: none;
    color: var(--ink);
    font-size: 19px;
  }
  .contact-list li {
    display: flex;
    align-items: center;
    height: 30px;
  }
  .contact-list li + li { margin-top: 2px; }
  .contact-list svg {
    width: 20px;
    height: 20px;
    margin-right: 17px;
    flex: none;
  }
  .address-band {
    position: absolute;
    left: 0;
    right: 0;
    top: 293px;
    height: 29px;
    background: var(--brand-green);
    color: var(--paper);
    font-size: 16px;
    line-height: 29px;
    text-align: center;
  }
</style>
</head>
<body>

  <section class="card card-front" aria-label="Card front">
    <div class="wordmark">KLV COURIER</div>
  </section>

  <section class="card card-back" aria-label="Card back">
    <div class="wordmark">KLV COURIER</div>

    <div class="identity">
      <p class="company">KLV COURIER</p>
      <p class="role">Managar</p>
    </div>

    <ul class="contact-list">
      <li>
        <svg viewBox="0 0 20 20" aria-hidden="true">
          <path d="M6 2.5 L8.5 6 L7 7.8 C8 10 10 12 12.2 13 L14 11.5 L17.5 14 L16 17 C10 17.5 2.5 10 3 4 Z" fill="none" stroke="var(--brand-green)" stroke-width="1.6" stroke-linejoin="round"/>
        </svg>
        <span>044- 444 444, 044 - 44444</span>
      </li>
      <li>
        <svg viewBox="0 0 20 20" aria-hidden="true">
          <rect x="2" y="4.5" width="16" height="11" fill="none" stroke="var(--brand-green)" stroke-width="1.5"/>
          <path d="M2 4.5 L10 11 L18 4.5 M2 15.5 L8 9.5 M18 15.5 L12 9.5" fill="none" stroke="var(--brand-green)" stroke-width="1.3"/>
        </svg>
        <span>info@klv.com</span>
      </li>
      <li>
        <svg viewBox="0 0 20 20" aria-hidden="true">
          <circle cx="10" cy="10" r="7.5" fill="none" stroke="var(--brand-green)" stroke-width="1.5"/>
          <ellipse cx="10" cy="10" rx="3.2" ry="7.5" fill="none" stroke="var(--brand-green)" stroke-width="1.2"/>
          <path d="M2.5 10 H17.5" stroke="var(--brand-green)" stroke-width="1.2"/>
        </svg>
        <span>www.klv.com</span>
      </li>
    </ul>

    <div class="address-band">address. address. address. address. address. address. address. address.</div>
  </section>

</body>
</html>
```